Commercial Real Estate

We need a business card design for a new commercial real estate business that specializes in apartment building brokerage. Not individual units but the entire complex. We find and represent the owners existing buildings and well as new buyers for those buildings. The design should convey trust, integrity, knowledge and growth. It should be easily read.

Target Market(s)

40 to 65 years old

Industry/Entity Type

Real Estate

```html
<!DOCTYPE html>
<html lang="en">
<head>
<meta charset="utf-8">
<title>Harborline Property Investments — Business Card</title>
<link href="https://fonts.googleapis.com/css2?family=Cinzel:wght@400;700&display=swap" rel="stylesheet">
<style>
  :root {
    --slate: #5b6a6a;
    --slate-dark: #4f5d5d;
    --teal: #6ccfc8;
    --mist: #a9b0b2;
    --paper: #ffffff;
    --paper-shade: #eef0f0;
    --backdrop: #e4e6e6;
    --ink-light: #f4f6f6;
  }
  * { box-sizing: border-box; margin: 0; padding: 0; }
  html, body { width: 1200px; height: 900px; overflow: hidden; }
  body {
    background: var(--backdrop);
    font-family: "Cinzel", Georgia, serif;
    display: flex;
    flex-direction: column;
    align-items: center;
    justify-content: center;
    gap: 48px;
  }
  .card {
    position: relative;
    width: 640px;
    height: 366px;
    border-radius: 28px;
    overflow: hidden;
    background: linear-gradient(180deg, var(--paper) 0%, var(--paper-shade) 100%);
    box-shadow: 0 10px 28px rgba(0,0,0,0.18);
  }
  .card-art { position: absolute; inset: 0; width: 100%; height: 100%; }

  .brand {
    position: absolute;
    display: flex;
    flex-direction: column;
    align-items: center;
    color: var(--slate);
  }
  .brand-row { display: flex; align-items: center; gap: 10px; }
  .brand-mark { width: 16px; height: 16px; background: var(--teal); }
  .brand-name { font-weight: 700; font-size: 26px; letter-spacing: 1px; }
  .brand-tagline { font-weight: 700; font-size: 10px; letter-spacing: 1px; margin-top: 2px; }

  .front .brand { left: 50%; top: 62px; transform: translateX(-50%); }
  .back .brand { left: 330px; top: 120px; }

  .holder { position: absolute; left: 56px; top: 200px; color: var(--ink-light); }
  .holder-name { font-size: 19px; letter-spacing: 1px; }
  .holder-title { font-size: 15px; letter-spacing: 1px; margin-top: 2px; }

  .contacts {
    position: absolute;
    left: 392px;
    top: 244px;
    list-style: none;
    color: var(--ink-light);
    font-size: 12.5px;
    line-height: 15.5px;
  }
  .contacts li { display: flex; align-items: flex-start; gap: 7px; }
  .contacts .icon { width: 12px; height: 12px; margin-top: 1.5px; flex: none; }
  .contacts .indent { padding-left: 19px; }

  .web-curve { font-family: "Cinzel", Georgia, serif; font-size: 14px; letter-spacing: 2px; fill: var(--ink-light); }
</style>
</head>
<body>

  <section class="card back" aria-label="Card back">
    <svg class="card-art" viewBox="0 0 640 366">
      <path d="M0,0 H200 C250,170 420,300 640,322 V366 H0 Z" fill="var(--mist)"/>
      <path d="M0,0 H178 C226,176 410,312 640,342 V366 H0 Z" fill="var(--slate)"/>
      <path id="web-path" d="M60,20 C110,150 230,250 420,320" fill="none"/>
      <text class="web-curve"><textPath href="#web-path" startOffset="4%">www.harborlinepi.com</textPath></text>
    </svg>
    <div class="brand">
      <div class="brand-row">
        <span class="brand-mark"></span>
        <span class="brand-name">HARBORLINE</span>
      </div>
    </div>
  </section>

  <section class="card front" aria-label="Card front">
    <svg class="card-art" viewBox="0 0 640 366">
      <path d="M0,150 C200,160 420,210 640,225 V366 H0 Z" fill="var(--teal)"/>
      <path d="M0,160 C200,170 420,220 640,235 V366 H0 Z" fill="var(--slate)"/>
      <path d="M128,164 L152,166 L140,182 Z" fill="var(--slate)"/>
    </svg>

    <div class="brand">
      <div class="brand-row">
        <span class="brand-mark"></span>
        <span class="brand-name">HARBORLINE</span>
      </div>
      <span class="brand-tagline">Property Investments</span>
    </div>

    <div class="holder">
      <p class="holder-name">Daniel Reyes</p>
      <p class="holder-title">Owner / C.E.O</p>
    </div>

    <ul class="contacts">
      <li>
        <svg class="icon" viewBox="0 0 12 12"><circle cx="6" cy="6" r="6" fill="var(--ink-light)"/><path d="M3,6.5 L6,3.5 L9,6.5 V9 H3 Z" fill="var(--slate)"/></svg>
        <span>Suite # 410, Elm Bldg.</span>
      </li>
      <li class="indent">NY 10452</li>
      <li>
        <svg class="icon" viewBox="0 0 12 12"><circle cx="6" cy="6" r="6" fill="var(--ink-light)"/><path d="M3.5,3 L5,3 L5.6,4.8 L4.7,5.6 C5.2,6.6 5.6,7 6.5,7.4 L7.2,6.5 L9,7.1 V8.6 C6,9 3.2,6.4 3.5,3 Z" fill="var(--slate)"/></svg>
        <span>555-201-4480</span>
      </li>
      <li>
        <svg class="icon" viewBox="0 0 12 12"><circle cx="6" cy="6" r="6" fill="var(--ink-light)"/><rect x="4.2" y="2.5" width="3.6" height="7" rx="0.7" fill="var(--slate)"/></svg>
        <span>555-310-7725</span>
      </li>
      <li>
        <svg class="icon" viewBox="0 0 12 12"><circle cx="6" cy="6" r="6" fill="var(--ink-light)"/><rect x="3" y="5" width="6" height="3.5" fill="var(--slate)"/><rect x="4" y="3" width="4" height="2" fill="var(--slate)"/></svg>
        <span>555-418-9036</span>
      </li>
      <li>
        <svg class="icon" viewBox="0 0 12 12"><circle cx="6" cy="6" r="6" fill="var(--ink-light)"/><rect x="3" y="4" width="6" height="4.2" fill="var(--slate)"/><path d="M3,4 L6,6.4 L9,4" fill="none" stroke="var(--ink-light)" stroke-width="0.7"/></svg>
        <span>name@harborlinepi.com</span>
      </li>
      <li>
        <svg class="icon" viewBox="0 0 12 12"><circle cx="6" cy="6" r="6" fill="var(--ink-light)"/><circle cx="6" cy="6" r="3.2" fill="none" stroke="var(--slate)" stroke-width="0.9"/><path d="M2.8,6 H9.2 M6,2.8 V9.2" stroke="var(--slate)" stroke-width="0.8"/></svg>
        <span>www.harborlinepi.com</span>
      </li>
    </ul>
  </section>

</body>
</html>
```